Breezeway Comfort business cards design

Need a business card design for a Heating and Air Conditioning business. I need these items included.
Business name: Breezeway Comfort
Owner: Marcus Tollefsen
License # 2874590
Phone number # 555-382-4071
Email: breezewaycomfortair@mailvista.example
Sales
Service
Installation
Maintenance

Heating and Air Conditioning

Requirements
Must have
• Company name , license number , phone number , email

```html
<!DOCTYPE html>
<html lang="en">
<head>
<meta charset="utf-8">
<title>Breezeway Comfort – Business Cards</title>
<link rel="stylesheet" href="https://fonts.googleapis.com/css2?family=Montserrat:wght@400;500;600;700;800&display=swap">
<style>
  :root{
    --bg:#d2d2d4;
    --card:#ffffff;
    --navy:#243a8f;
    --band:#2f52a8;
    --pink:#e8376f;
    --orange:#f5a13f;
    --white:#ffffff;
    --faint:#f4ede6;
  }
  *{box-sizing:border-box;margin:0;padding:0}
  html,body{width:1200px;height:1200px;overflow:hidden;background:var(--bg);font-family:"Montserrat",sans-serif}
  .canvas{position:relative;width:1200px;height:1200px}
  .card{position:absolute;left:180px;width:840px;height:480px;background:var(--card);overflow:hidden;box-shadow:0 12px 30px rgba(0,0,0,.12)}
  .card--front{top:90px}
  .card--back{top:630px}

  /* front */
  .brand{position:absolute;left:70px;top:78px;display:flex;align-items:center;gap:14px}
  .brand__dot{width:34px;height:34px;border-radius:50%;background:var(--orange)}
  .brand__name{font-size:30px;font-weight:800;color:var(--navy);letter-spacing:1px;text-transform:uppercase;line-height:1}
  .deco-circle{position:absolute;right:-90px;top:-110px;width:420px;height:420px;border-radius:50%;background:var(--faint)}
  .name-tab{position:absolute;left:70px;top:250px;width:440px;height:100px;border-radius:26px 26px 0 0;
    background:linear-gradient(90deg,var(--pink),var(--orange));padding:22px 30px;color:var(--white)}
  .name-tab__name{font-size:32px;font-weight:700;text-transform:uppercase;letter-spacing:.5px;line-height:1}
  .name-tab__license{font-size:12px;font-weight:500;margin-top:6px}
  .contact-band{position:absolute;left:0;top:340px;width:100%;height:100px;background:var(--band);
    display:flex;align-items:center;padding:0 40px 0 82px;gap:44px;color:var(--white)}
  .contact{display:flex;align-items:center;gap:14px;font-size:20px;font-weight:500;white-space:nowrap}
  .contact__icon{width:34px;height:34px;flex:none}

  /* back */
  .back-brand{position:absolute;left:0;right:0;top:80px;text-align:center;color:var(--navy);font-weight:800;text-transform:uppercase}
  .back-brand__name{font-size:54px;letter-spacing:2px;line-height:1.05}
  .back-brand__line{font-size:26px;letter-spacing:6px;margin-top:14px}
  .services-band{position:absolute;left:0;top:320px;width:100%;height:100px;background:var(--band);
    display:flex;align-items:center;justify-content:center;color:var(--white);font-size:28px;font-weight:600;letter-spacing:1px;text-transform:uppercase}
</style>
</head>
<body>
<main class="canvas">
  <section class="card card--front" aria-label="Business card front">
    <div class="deco-circle" aria-hidden="true"></div>
    <div class="brand">
      <span class="brand__dot" aria-hidden="true"></span>
      <span class="brand__name">Breezeway Comfort</span>
    </div>
    <div class="name-tab">
      <p class="name-tab__name">Marcus Tollefsen</p>
      <p class="name-tab__license">License # 2874590</p>
    </div>
    <div class="contact-band">
      <div class="contact">
        <svg class="contact__icon" viewBox="0 0 34 34" aria-hidden="true">
          <circle cx="17" cy="17" r="17" fill="#fff"/>
          <path d="M12 10c1-1 2-1 2.6 0l1.6 2.6c.4.7.2 1.4-.4 1.9l-1 .8c.8 1.9 2.1 3.2 4 4l.8-1c.5-.6 1.2-.8 1.9-.4l2.6 1.6c1 .6 1 1.6 0 2.6l-1 1c-1 1-3 1-5.5-.5-2.6-1.6-4.8-3.8-6.3-6.3C9.8 13.8 9.9 12 11 11z" fill="#2f52a8"/>
        </svg>
        <span>555-382-4071</span>
      </div>
      <div class="contact">
        <svg class="contact__icon" viewBox="0 0 34 34" aria-hidden="true">
          <circle cx="17" cy="17" r="17" fill="#fff"/>
          <rect x="9" y="11.5" width="16" height="11" rx="1.5" fill="#2f52a8"/>
          <path d="M9.5 12.5l7.5 5.5 7.5-5.5" fill="none" stroke="#fff" stroke-width="1.4"/>
        </svg>
        <span>breezewaycomfortair@mailvista.example</span>
      </div>
    </div>
  </section>

  <section class="card card--back" aria-label="Business card back">
    <div class="back-brand">
      <p class="back-brand__name">Breezeway Comfort</p>
      <p class="back-brand__line">Heating &amp; Air</p>
    </div>
    <div class="services-band">Sales, Service, Installation &amp; Maintenance</div>
  </section>
</main>
</body>
</html>
```